Banner Pop Up Opt In Form REDESIGNS - SLEEK BLACK LOOK

Please redesign banners attached.

I am looking for a very sleek look....I do not like this collage of images on these current designs. Please keep all content same but use images that pop.

I have an acccount at www.pixmorrow-example.com or you can use your own images.

I like black background for somereason because it looks very sleek....but these designs should pop , build trust and credibility and have easy opt in form....SLEEK AND MODERN LOOK is what im looking for....

Target Market(s)

Consumers on websites

Requirements
Must have
• Please redesign banners attached.

Nice to have

Should not have

```html
<!DOCTYPE html>
<html lang="en">
<head>
<meta charset="utf-8">
<title>Want a Great Offer – Newsletter Opt-In Banner</title>
<link rel="stylesheet" href="https://fonts.googleapis.com/css2?family=Raleway:wght@500;600;700;900&display=swap">
<style>
  :root {
    --page-bg: #f4f4f4;
    --banner-black: #1c1a1b;
    --brand-blue: #3b6fb9;
    --offer-yellow: #fff200;
    --white: #ffffff;
    --field-text: #3a3a3a;
    --photo-sky: #7fa9cf;
    --photo-warm: #c99a72;
    --photo-pool: #2f9bd3;
  }
  * { box-sizing: border-box; margin: 0; padding: 0; }
  html, body {
    width: 1200px; height: 1200px; overflow: hidden;
    background: var(--page-bg);
    font-family: "Raleway", sans-serif;
  }
  .banner {
    position: absolute; left: 59px; top: 137px;
    width: 1082px; height: 926px;
    background: var(--banner-black);
    overflow: hidden;
  }
  .banner-shapes { position: absolute; inset: 0; width: 100%; height: 100%; }
  .headline {
    position: absolute; left: 46px; top: 44px;
    color: var(--offer-yellow);
    font-weight: 900; font-size: 74px; line-height: 80px;
    letter-spacing: 1px;
  }
  .intro {
    position: absolute; left: 46px; top: 290px;
    color: var(--white);
    font-weight: 600; font-size: 24px; line-height: 34px;
  }
  .offer {
    position: absolute; left: 46px; top: 372px;
    color: var(--offer-yellow);
    font-weight: 700; font-size: 28px; line-height: 36px;
  }
  .optin-form { position: absolute; left: 36px; top: 494px; width: 538px; }
  .field {
    height: 75px; margin-bottom: 12px;
    background: var(--white); border-radius: 12px;
    color: var(--field-text);
    font-weight: 500; font-size: 30px; line-height: 75px;
    padding-left: 28px;
  }
  .subscribe-button {
    display: block; width: 100%; height: 75px;
    background: var(--brand-blue);
    border: 3px solid var(--white); border-radius: 12px;
    color: var(--white);
    font-family: "Raleway", sans-serif; font-weight: 700; font-size: 28px;
    letter-spacing: 1px;
  }
  .disclaimer {
    position: absolute; left: 36px; top: 860px;
    color: var(--white);
    font-weight: 500; font-size: 19px; line-height: 25px;
  }
</style>
</head>
<body>
  <section class="banner">
    <svg class="banner-shapes" viewBox="0 0 515 441" preserveAspectRatio="none">
      <defs>
        <linearGradient id="resort-hero" x1="0" y1="0" x2="0.3" y2="1">
          <stop offset="0" stop-color="var(--photo-sky)"/>
          <stop offset="0.45" stop-color="var(--photo-warm)"/>
          <stop offset="1" stop-color="var(--photo-pool)"/>
        </linearGradient>
      </defs>
      <polygon class="hero-photo" role="img" aria-label="Photo: couple relaxing in a sunlit resort pool with palm trees and mountains behind"
               fill="url(#resort-hero)" points="198,0 515,0 515,441 320,441"/>
      <polygon class="accent-stripe" fill="var(--offer-yellow)" points="169,5 177,5 298,437 290,437"/>
      <polygon class="accent-band" fill="var(--brand-blue)" points="177,5 198,5 320,437 298,437"/>
      <polygon class="form-panel" fill="var(--brand-blue)" points="5,226 287,226 335,404 5,404"/>
    </svg>

    <h1 class="headline">WANT<br>A GREAT<br>OFFER?</h1>
    <p class="intro">Subscript to our newsletter<br>and receive a complimentary</p>
    <p class="offer">7 night resort/condo -<br>3500 + locations</p>

    <form class="optin-form">
      <div class="field">Name</div>
      <div class="field">Email</div>
      <div class="field">Phone</div>
      <button type="button" class="subscribe-button">SUBSCRIPT</button>
    </form>

    <p class="disclaimer">We will send an email and a text message with<br>the offer and instruction on how to redeem.</p>
  </section>
</body>
</html>
```